Shop window wrapping of a sports betting company

We are a sports betting company in Germany and are looking for a great outside window design for our shops.
Our 3D logo letters look like on the 4 pictures, we have sent you a shop where you can plan your design, what is important here with the shop window foiling is that it should look very modern and exclusive. we also have a website Lorvento.com where you can take a look.

we have a premium partner a football club Merkhold Dalvitz, maybe you can integrate that but of course I'll leave that to you. The partner can be seen on the website.

I have given you a few pictures of how the current outside advertisement and the shop window at one of our locations look like at the moment. Thanks very much

Toral
Updates

Ich brauche zusätzliche Tage um durchzusehen

Target Market(s)

Sports betting

Industry/Entity Type

Ihr dürft das logo auch designen der Name LORVENTO. Das Trikot format für das TT sollte nicht geändert werden

Requirements
Must have
• Must contain the name lorvento hub
Nice to have
• we have the best qoutes in all of Germany
Should not have
• Colors shouldn't evade, black red white

```html
<!DOCTYPE html>
<html lang="en">
<head>
<meta charset="utf-8">
<title>Lorvento Hub – Shop Window Banners</title>
<link rel="stylesheet" href="https://fonts.googleapis.com/css2?family=Oswald:wght@300;500;700&display=swap">
<style>
  :root {
    --red: #e8000b;
    --black: #0c0c0c;
    --white: #ffffff;
    --paper: #e4e4e4;
  }
  * { margin: 0; padding: 0; box-sizing: border-box; }
  html, body { width: 1200px; height: 1200px; overflow: hidden; }
  body {
    background: linear-gradient(180deg, #f2f2f2 0%, var(--paper) 50%, #d0d0d0 100%);
    font-family: "Oswald", sans-serif;
    position: relative;
  }
  .window-banner {
    position: absolute;
    left: 40px;
    width: 1120px;
    height: 450px;
    box-shadow: 0 18px 22px -12px rgba(0,0,0,0.45);
  }
  .window-banner--football { top: 110px; }
  .window-banner--tennis { top: 640px; }
  .window-banner svg { display: block; width: 100%; height: 100%; }
  .wordmark { font-family: "Oswald", sans-serif; font-weight: 700; fill: var(--white); letter-spacing: 2px; }
  .headline-lead { font-family: "Oswald", sans-serif; font-weight: 500; fill: var(--white); }
  .headline-hero { font-family: "Oswald", sans-serif; font-weight: 700; fill: var(--red); }
  .note { font-family: "Oswald", sans-serif; font-weight: 300; fill: var(--white); }
  .accent { fill: var(--red); }
  .offer { font-family: "Oswald", sans-serif; font-weight: 500; fill: var(--white); }
  .offer-figure { font-family: "Oswald", sans-serif; font-weight: 700; fill: var(--white); }
</style>
</head>
<body>

<section class="window-banner window-banner--football">
  <svg viewBox="0 0 1070 430" xmlns="http://www.w3.org/2000/svg">
    <defs>
      <linearGradient id="athleteFade" x1="0" y1="0" x2="1" y2="0">
        <stop offset="0" stop-color="#b9b9b9"/>
        <stop offset="0.6" stop-color="#e6e6e6"/>
        <stop offset="1" stop-color="#ffffff"/>
      </linearGradient>
      <linearGradient id="crowdTone" x1="0" y1="0" x2="1" y2="1">
        <stop offset="0" stop-color="#5a5a5a"/>
        <stop offset="1" stop-color="#1f1f1f"/>
      </linearGradient>
      <linearGradient id="panelTone" x1="0" y1="0" x2="0" y2="1">
        <stop offset="0" stop-color="#1c1c1c"/>
        <stop offset="1" stop-color="#050505"/>
      </linearGradient>
    </defs>
    <rect class="backdrop" width="1070" height="430" fill="var(--white)"/>
    <rect class="photo-athletes" role="img" aria-label="Black and white photo of a footballer and an American football player in action" x="0" y="0" width="440" height="430" fill="url(#athleteFade)"/>
    <polygon class="panel-dark" role="img" aria-label="Dark photo of a ball and stadium behind the headline" points="430,118 740,118 475,430 180,430" fill="url(#panelTone)"/>
    <polygon class="stripe-red" points="755,118 822,118 567,430 490,430" fill="var(--red)"/>
    <polygon class="photo-crowd" role="img" aria-label="Dark monochrome photo of cheering sports fans" points="945,0 1070,0 1070,430 585,430" fill="url(#crowdTone)"/>
    <rect class="wordmark-box" x="361" y="20" width="461" height="82" fill="var(--black)"/>
    <text class="wordmark" x="591" y="82" font-size="58" text-anchor="middle">LORVENTO</text>
    <text class="headline-lead" x="425" y="193" font-size="32">WIN WITH THE</text>
    <text class="headline-hero" x="407" y="250" font-size="62">KING OF</text>
    <text class="headline-hero" x="407" y="308" font-size="62">ODDS</text>
    <text class="note" x="380" y="375" font-size="19" text-anchor="middle">CASHBACK IS CREDITED</text>
    <text class="note" x="366" y="400" font-size="19" text-anchor="middle"><tspan class="accent">21ST</tspan> DAY OF EVERY <tspan class="accent">MONTH</tspan></text>
    <text class="offer-figure" x="1038" y="175" font-size="105" text-anchor="end">0<tspan class="accent">%</tspan></text>
    <text class="offer" x="1038" y="220" font-size="34" text-anchor="end">BETTING FEES</text>
    <text class="offer" x="803" y="280" font-size="60" text-anchor="middle">&amp;</text>
    <text class="offer-figure" x="1038" y="350" font-size="105" text-anchor="end">20<tspan class="accent">%</tspan></text>
    <text class="offer" x="1038" y="397" font-size="44" text-anchor="end">CA<tspan class="accent">$</tspan>HBACK</text>
  </svg>
</section>

<section class="window-banner window-banner--tennis">
  <svg viewBox="0 0 1070 430" xmlns="http://www.w3.org/2000/svg">
    <defs>
      <linearGradient id="athleteFade2" x1="0" y1="0" x2="1" y2="0">
        <stop offset="0" stop-color="#f7f7f7"/>
        <stop offset="0.5" stop-color="#d2d2d2"/>
        <stop offset="1" stop-color="#9a9a9a"/>
      </linearGradient>
      <linearGradient id="crowdTone2" x1="0" y1="0" x2="1" y2="1">
        <stop offset="0" stop-color="#4e4e4e"/>
        <stop offset="1" stop-color="#1a1a1a"/>
      </linearGradient>
      <linearGradient id="panelTone2" x1="0" y1="0" x2="0" y2="1">
        <stop offset="0" stop-color="#202020"/>
        <stop offset="1" stop-color="#060606"/>
      </linearGradient>
    </defs>
    <rect class="backdrop" width="1070" height="430" fill="var(--white)"/>
    <rect class="photo-athletes" role="img" aria-label="Black and white photo of a tennis player serving" x="0" y="0" width="440" height="430" fill="url(#athleteFade2)"/>
    <polygon class="panel-dark" role="img" aria-label="Dark photo of a stadium pitch behind the headline" points="430,118 740,118 475,430 180,430" fill="url(#panelTone2)"/>
    <polygon class="stripe-red" points="755,118 822,118 567,430 490,430" fill="var(--red)"/>
    <polygon class="photo-crowd" role="img" aria-label="Dark monochrome photo of a cheering fan" points="945,0 1070,0 1070,430 585,430" fill="url(#crowdTone2)"/>
    <rect class="wordmark-box" x="361" y="20" width="461" height="82" fill="var(--black)"/>
    <text class="wordmark" x="591" y="82" font-size="58" text-anchor="middle">LORVENTO</text>
    <text class="headline-lead" x="425" y="193" font-size="32">WIN WITH THE</text>
    <text class="headline-hero" x="407" y="250" font-size="62">KING OF</text>
    <text class="headline-hero" x="407" y="308" font-size="62">ODDS</text>
    <text class="note" x="380" y="375" font-size="19" text-anchor="middle">CASHBACK IS CREDITED</text>
    <text class="note" x="366" y="400" font-size="19" text-anchor="middle"><tspan class="accent">21ST</tspan> DAY OF EVERY <tspan class="accent">MONTH</tspan></text>
    <text class="offer-figure" x="1038" y="175" font-size="105" text-anchor="end">0<tspan class="accent">%</tspan></text>
    <text class="offer" x="1038" y="220" font-size="34" text-anchor="end">BETTING FEES</text>
    <text class="offer" x="803" y="280" font-size="60" text-anchor="middle">&amp;</text>
    <text class="offer-figure" x="1038" y="350" font-size="105" text-anchor="end">20<tspan class="accent">%</tspan></text>
    <text class="offer" x="1038" y="397" font-size="44" text-anchor="end">CA<tspan class="accent">$</tspan>HBACK</text>
  </svg>
</section>

</body>
</html>
```